'Bright Ledger Hidden Keys' Book Cover

I need a professional book cover design for my new upcoming book that shows people how to get a high credit score.

Here are my two websites:

https://www.moneywordbank-lexa.info
https://moneywordbank-lexa.com/

I am looking for a clean, professional design that pops (emotional touch) and separates from the other books that are on the market. Cover aspect ratio 1:4 for Pagewisp version and 1:5 for the paperback version. Yellow or blue are good colors - but not must. See the basic examples that I provided. File delivery format PDF.

Book Title: Bright Ledger Hidden Keys
Byline: The Quick Lift And Mend Manual for Stellar Borrowing

Currently on Brindlecart pre-order:
https://www.brindlecart.example/Bright-Ledger-Hidden-Keys-Stellar-ebook/dp/Q48MPLRT71

I am the author of 36 published books on Brindlecart. My author profile is here:
brindlecart.example/author/gideonvarly

Targeted audience: People that want to improve or repair their bad credit score.

Target Market(s)

People/consumers in the US that want to improve or repair their credit score.

Industry/Entity Type

Consumer

Font styles to use
Sans Serif

Colors

Designer to choose colors to be used in the design.

Requirements
Must have
• Author name, Title, byline, and graphic element(s).
Nice to have
• - 2020 edition logo / batch

```html
<!DOCTYPE html>
<html lang="en">
<head>
<meta charset="utf-8">
<title>Bright Ledger Hidden Keys – Book Cover</title>
<link rel="stylesheet" href="https://fonts.googleapis.com/css2?family=Jost:wght@400;600;700&display=swap">
<style>
  :root {
    --stage: #efefef;
    --cover-yellow: #f6ec34;
    --band-navy: #063766;
    --title-navy: #0b3562;
    --ink-black: #111111;
    --photo-bright: #fbfbfc;
    --photo-soft: #dfe2e8;
    --photo-shade: #9aa6b8;
  }
  html, body {
    margin: 0;
    padding: 0;
    width: 1200px;
    height: 800px;
    overflow: hidden;
    background: var(--stage);
  }
  .canvas {
    position: relative;
    width: 1200px;
    height: 800px;
    display: flex;
    align-items: center;
    justify-content: center;
  }
  .cover {
    position: relative;
    width: 436px;
    height: 720px;
    background: var(--cover-yellow);
    overflow: hidden;
    box-shadow: 0 2px 6px rgba(0,0,0,0.12);
  }
  .cover__author {
    position: absolute;
    top: 26px;
    left: 0;
    right: 0;
    margin: 0;
    text-align: center;
    font-family: 'Jost', sans-serif;
    font-weight: 600;
    font-size: 23px;
    letter-spacing: 0.2em;
    color: var(--ink-black);
  }
  .cover__title {
    position: absolute;
    top: 104px;
    left: 55px;
    right: 14px;
    margin: 0;
    font-family: 'Jost', sans-serif;
    font-weight: 700;
    color: var(--title-navy);
    line-height: 1;
    text-transform: uppercase;
  }
  .cover__title-line { display: block; }
  .cover__title-line--lead {
    font-size: 42px;
    letter-spacing: 0.01em;
    margin-bottom: 16px;
  }
  .cover__title-line--big {
    font-size: 84px;
    letter-spacing: 0.005em;
    margin-bottom: 12px;
  }
  .cover__subtitle {
    position: absolute;
    top: 382px;
    left: 55px;
    right: 14px;
    margin: 0;
    font-family: 'Jost', sans-serif;
    font-weight: 400;
    font-size: 21px;
    line-height: 1.5;
    color: var(--ink-black);
    text-transform: uppercase;
  }
  .cover__band {
    position: absolute;
    left: 0;
    right: 0;
    top: 468px;
    bottom: 0;
    background: var(--band-navy);
  }
  .cover__photo {
    position: absolute;
    left: 24px;
    top: 450px;
    width: 372px;
    height: 270px;
    background:
      radial-gradient(ellipse 32% 48% at 82% 78%, var(--photo-bright) 0%, var(--photo-soft) 55%, rgba(223,226,232,0) 100%),
      radial-gradient(ellipse 42% 62% at 38% 60%, var(--photo-bright) 0%, var(--photo-soft) 45%, var(--photo-shade) 70%, rgba(154,166,184,0) 100%);
  }
</style>
</head>
<body>
  <main class="canvas">
    <article class="cover">
      <p class="cover__author">GIDEON VARLY</p>
      <h1 class="cover__title">
        <span class="cover__title-line cover__title-line--lead">Bright Ledger</span>
        <span class="cover__title-line cover__title-line--big">Hidden</span>
        <span class="cover__title-line cover__title-line--big">Keys</span>
      </h1>
      <p class="cover__subtitle">The Quick Lift And Mend<br>Manual for Stellar Borrowing</p>
      <div class="cover__band"></div>
      <div class="cover__photo" role="img" aria-label="Photo of a delighted woman in a white blazer holding a card and cheering beside a white laptop"></div>
    </article>
  </main>
</body>
</html>
```